Pelbrook Metal Roofing INC.

Hello,
I am working with a local business to design them a new website. The designer I had worked with moved to colorado and has taken a new job. He recommended that I try posting my new jobs on here. I would need a design and assistance setting the site up on my host nimbus server. I work by myself and handle the sales side of things and need a designer that can help me out.
This company is a metal roofing business. The current page I made for them is www.pelbrookmetalinc.example

They would like the new site to be similar to http://www.tamblecreekalloy.example

Please let me know if this is something that you could do for us.
Updates

the company wants the site to look very similar to this http://www.tamblecreekalloy.exampleis that something you could do, please get in touch with me.Thanks Added Tuesday, January 10, 2017

Industry/Entity Type

Business

Font styles to use
Sans Serif

Colors
ed252d

Requirements
Must have
• the company wants the site to look very similar to this
• http://www.tamblecreekalloy.example
• is that something you could do, please get in touch with me.
• Thanks

```html
<!DOCTYPE html>
<html lang="en">
<head>
<meta charset="utf-8">
<title>Pelbrook Metal Inc</title>
<link rel="stylesheet" href="https://fonts.googleapis.com/css2?family=Open+Sans:wght@400;600;700;800&display=swap">
<style>
  :root {
    --red: #ed252d;
    --ink: #222428;
    --text: #55585e;
    --muted: #8a8d92;
    --line: #e3e3e3;
    --footer: #efefef;
    --white: #ffffff;
    --sky-top: #5f8fbf;
    --sky-low: #b9cfe2;
    --roof: #2d3138;
  }
  * { box-sizing: border-box; margin: 0; padding: 0; }
  html, body { width: 849px; height: 1200px; overflow: hidden; }
  body { font-family: "Open Sans", Arial, sans-serif; color: var(--text); background: var(--white); position: relative; }

  .site-header { position: absolute; top: 0; left: 0; width: 849px; height: 50px; background: var(--white); border-bottom: 1px solid var(--line); }
  .brand { position: absolute; left: 90px; top: 15px; font-size: 17px; font-weight: 800; color: var(--red); letter-spacing: .3px; }
  .main-nav { position: absolute; left: 312px; top: 0; display: flex; gap: 22px; height: 50px; align-items: center; font-size: 13px; color: var(--ink); }
  .main-nav .active { color: var(--red); position: relative; }
  .main-nav .active::after { content: ""; position: absolute; left: -8px; right: -8px; bottom: -17px; height: 2px; background: var(--red); }
  .header-phone { position: absolute; left: 648px; top: 16px; display: flex; align-items: center; gap: 6px; font-size: 14px; font-weight: 700; color: var(--red); }

  .hero { position: absolute; top: 50px; left: 0; width: 849px; height: 376px; background: linear-gradient(180deg, var(--sky-top) 0%, var(--sky-low) 45%, #6e7580 62%, var(--roof) 100%); }
  .hero-title { position: absolute; left: 90px; top: 165px; font-size: 26px; line-height: 32px; font-weight: 800; color: var(--white); text-transform: uppercase; }
  .hero-arrow { position: absolute; top: 168px; }
  .hero-arrow.prev { left: 44px; }
  .hero-arrow.next { right: 44px; }
  .feature-tabs { position: absolute; left: 88px; top: 312px; width: 675px; height: 64px; display: flex; }
  .feature-tab { flex: 1; text-align: center; padding-top: 16px; background: rgba(235,235,235,.92); border-right: 1px solid #d2d2d2; }
  .feature-tab:last-child { border-right: 0; }
  .feature-tab.current { background: #2a2c30; }
  .feature-tab h3 { font-size: 15px; font-weight: 400; color: #555; }
  .feature-tab p { font-size: 9px; color: #888; margin-top: 2px; }
  .feature-tab.current h3 { color: var(--white); }
  .feature-tab.current p { color: #bbb; }

  .intro { position: absolute; top: 474px; left: 0; width: 849px; text-align: center; }
  .intro h2 { font-size: 20px; font-weight: 600; color: var(--ink); letter-spacing: .2px; }
  .intro p { width: 560px; margin: 14px auto 0; font-size: 11px; line-height: 18px; color: var(--text); }

  .service-cards { position: absolute; top: 617px; left: 93px; width: 665px; display: flex; gap: 24px; }
  .service-card { width: 206px; height: 228px; background: var(--white); box-shadow: 0 2px 8px rgba(0,0,0,.16); text-align: center; position: relative; }
  .card-media { height: 112px; }
  .media-frame { background: linear-gradient(180deg, #5d8ec4, #c49a5c); }
  .media-residential { background: linear-gradient(180deg, #8fb0cc, #6f737a); }
  .media-commercial { background: linear-gradient(180deg, #c9d7e2, #9b2a22); }
  .card-label { position: absolute; left: 35px; right: 35px; top: 100px; height: 26px; line-height: 26px; background: var(--red); color: var(--white); font-size: 12px; font-weight: 600; border-radius: 2px; }
  .card-text { padding: 24px 22px 0; font-size: 9.5px; line-height: 15px; color: var(--muted); }
  .card-button { position: absolute; left: 68px; bottom: 16px; width: 70px; height: 20px; line-height: 18px; border: 1px solid #bbb; font-size: 9px; color: var(--ink); }

  .site-footer { position: absolute; top: 935px; left: 0; width: 849px; height: 265px; background: var(--footer); }
  .footer-col { position: absolute; top: 36px; font-size: 9.5px; line-height: 17px; color: var(--text); }
  .footer-col h4 { font-size: 13px; font-weight: 600; color: var(--ink); margin-bottom: 8px; letter-spacing: .3px; }
  .col-company { left: 93px; }
  .col-resources { left: 225px; }
  .col-contact { left: 358px; }
  .col-newsletter { left: 540px; width: 220px; }
  .signup { display: flex; margin-bottom: 14px; }
  .signup span { flex: 1; height: 24px; line-height: 24px; padding-left: 8px; background: var(--white); color: #aaa; }
  .signup b { width: 74px; height: 24px; line-height: 24px; text-align: center; background: var(--red); color: var(--white); font-weight: 600; }
  .footer-bottom { position: absolute; left: 93px; right: 93px; top: 225px; border-top: 1px solid #d4d4d4; padding-top: 10px; text-align: center; font-size: 9px; color: var(--muted); }
</style>
</head>
<body>
  <header class="site-header">
    <div class="brand">PELBROOK METAL INC</div>
    <nav class="main-nav">
      <span class="active">Home</span><span>About Us</span><span>Services</span><span>Products</span><span>Contact</span>
    </nav>
    <div class="header-phone">
      <svg width="14" height="14" viewBox="0 0 14 14"><circle cx="7" cy="7" r="7" fill="#ed252d"/><path d="M4.6 3.8l1.2 1.4-.6.8c.5 1 1.3 1.8 2.3 2.3l.8-.6 1.4 1.2-.6 1.1c-2.6-.4-4.5-2.3-4.9-4.9z" fill="#fff"/></svg>
      (555) 014-0392
    </div>
  </header>

  <section class="hero" role="img" aria-label="Photo of a dark metal roof with a chimney under a blue sky">
    <svg class="hero-arrow prev" width="14" height="24" viewBox="0 0 14 24"><path d="M12 2L2 12l10 10" stroke="#fff" stroke-width="3" fill="none"/></svg>
    <svg class="hero-arrow next" width="14" height="24" viewBox="0 0 14 24"><path d="M2 2l10 10L2 22" stroke="#fff" stroke-width="3" fill="none"/></svg>
    <h1 class="hero-title">Quality Metal<br>Roofing Services</h1>
    <div class="feature-tabs">
      <div class="feature-tab current"><h3>Featured Service</h3><p>Panels cut to length</p></div>
      <div class="feature-tab"><h3>Featured Service</h3><p>Trims and flashing</p></div>
      <div class="feature-tab"><h3>Featured Service</h3><p>Fasteners and screws</p></div>
      <div class="feature-tab"><h3>Featured Service</h3><p>Gutters and downspouts</p></div>
    </div>
  </section>

  <section class="intro">
    <h2>MANUFACTURERS OF QUALITY BUILDING COMPONENTS</h2>
    <p>Durable metal roofing and siding panels crafted for homes, farms and commercial buildings. We supply trims, fasteners and custom lengths cut to order, with fast delivery across the region and friendly support from our experienced team at every step.</p>
  </section>

  <section class="service-cards">
    <article class="service-card">
      <div class="card-media media-frame" role="img" aria-label="Photo of timber post frame trusses against the sky"></div>
      <div class="card-label">Post Frame Building</div>
      <p class="card-text">Strong steel frames and trusses for barns, shops and garages built to last.</p>
      <div class="card-button">VIEW MORE</div>
    </article>
    <article class="service-card">
      <div class="card-media media-residential" role="img" aria-label="Photo of a house with a metal roof"></div>
      <div class="card-label">Residential Roofing</div>
      <p class="card-text">Long lasting metal roofs in many colors to protect and beautify your home.</p>
      <div class="card-button">VIEW MORE</div>
    </article>
    <article class="service-card">
      <div class="card-media media-commercial" role="img" aria-label="Photo of a worker installing a red metal roof"></div>
      <div class="card-label">Commercial Roofing</div>
      <p class="card-text">Heavy gauge panels and trims for warehouses, offices and industrial buildings.</p>
      <div class="card-button">VIEW MORE</div>
    </article>
  </section>

  <footer class="site-footer">
    <div class="footer-col col-company"><h4>COMPANY</h4>Home<br>About Us<br>Our Services<br>Gallery</div>
    <div class="footer-col col-resources"><h4>RESOURCES</h4>Support<br>Projects<br>Contact Us<br>Privacy Policy</div>
    <div class="footer-col col-contact"><h4>CONTACT US</h4>1200 Steel Creek Drive Suite 100<br>Springfield, ST 00000<br>(555) 014-0392<br>info@pelbrookmetal.example</div>
    <div class="footer-col col-newsletter">
      <h4>NEWSLETTER SIGN UP</h4>
      <div class="signup"><span>Email address</span><b>Subscribe</b></div>
      <h4>WORKING HOURS</h4>
      Monday - Friday: 7am - 5pm<br>Saturday: 8am - 12pm<br>Sunday: Closed
    </div>
    <div class="footer-bottom">© 2017 Company Name. All rights reserved. Terms of Use</div>
  </footer>
</body>
</html>
```